"Oral Surgery Office needs a Business Card Design with Logo"

We need a logo design and business card. The name of the office is Halvering Oral Surgery & Implant Center. The final design should communicate uniqueness as well as highly class office. The business card should emphasize power. I included the current business card below. Please design something unique

Target Market(s)

Dentists & Patients

Industry/Entity Type

Dental

Contact Information for Business Card

Unique Design to show success, prestige, Style, unmatched performance

Font styles to use
Serif

Colors
1b1b1b
ffffff
0556a4

Requirements
Must have
• Bussiness Name, Doctor's Name, Website, phone and Fax, email, office address
• Color should be either Black and White or Blue and White
Nice to have
• Clean look
Should not have
• the business card shouldn't be too busy. I feel like the old business card was too busy

```html
<!DOCTYPE html>
<html lang="en">
<head>
<meta charset="utf-8">
<title>Halvering Oral Surgery &amp; Implant Center — Business Card</title>
<link rel="stylesheet" href="https://fonts.googleapis.com/css2?family=Open+Sans:wght@400;600&family=Archivo+Narrow:wght@500&display=swap">
<style>
  :root {
    --backdrop: #2e2926;
    --card-black: #0b0b0b;
    --card-black-edge: #1b1b1b;
    --royal-blue: #1a1a8c;
    --ink-blue: #1f1f8f;
    --paper: #ffffff;
    --paper-shade: #d9d9d9;
    --text-light: #f2f2f2;
    --placeholder-light: #ececec;
    --placeholder-dark: #c8c8c8;
  }
  * { margin: 0; padding: 0; box-sizing: border-box; }
  html, body {
    width: 1200px; height: 844px; overflow: hidden;
    background: var(--backdrop);
  }
  .canvas {
    position: relative; width: 1200px; height: 844px;
    display: flex; align-items: center; justify-content: center; gap: 60px;
  }
  .card {
    position: relative; width: 500px; height: 286px; overflow: hidden;
    box-shadow: 0 14px 30px rgba(0,0,0,.45);
  }

  /* Back: contact side */
  .card--contact {
    background: linear-gradient(120deg, var(--card-black) 0%, var(--card-black-edge) 55%, #2a2a2a 100%);
    font-family: "Open Sans", sans-serif; color: var(--text-light);
  }
  .band { position: absolute; left: 0; width: 100%; height: 12px; background: var(--royal-blue); }
  .band--top { top: 18px; }
  .band--bottom { bottom: 18px; }
  .contact {
    position: absolute; inset: 0; display: flex; flex-direction: column;
    align-items: center; justify-content: center; text-align: center;
  }
  .contact__name { font-weight: 600; font-size: 17px; letter-spacing: .2px; }
  .contact__title { font-size: 12px; margin-bottom: 14px; }
  .contact__line { font-size: 13px; line-height: 1.45; }
  .contact__address { font-size: 13.5px; margin-top: 14px; }

  /* Front: brand side */
  .card--brand {
    background: radial-gradient(ellipse at 55% 40%, var(--paper) 30%, var(--paper-shade) 100%);
  }
  .tab { position: absolute; width: 30px; height: 50px; background: var(--royal-blue); }
  .tab--right { right: 0; top: 42px; }
  .tab--left { left: 0; top: 160px; }
  .brand {
    position: absolute; left: 90px; top: 60px; display: flex; align-items: center; gap: 16px;
  }
  .brand__illustration {
    width: 84px; height: 84px;
    background: linear-gradient(160deg, var(--placeholder-light), var(--placeholder-dark));
  }
  .brand__name {
    font-family: "Archivo Narrow", sans-serif; font-weight: 500;
    color: var(--ink-blue); font-size: 24px; line-height: 1.02; text-transform: uppercase;
  }
  .brand__line { display: block; white-space: nowrap; }
  .social {
    position: absolute; right: 70px; top: 196px; text-align: center;
    font-family: "Open Sans", sans-serif; font-size: 12px; color: var(--ink-blue);
    display: flex; flex-direction: column; gap: 10px; align-items: center;
  }
  .social__item { display: flex; align-items: center; gap: 5px; }
  .social__dot { width: 10px; height: 10px; background: var(--ink-blue); }
  .social__dot--round { border-radius: 50%; }
</style>
</head>
<body>
<main class="canvas">
  <section class="card card--contact">
    <div class="band band--top"></div>
    <div class="band band--bottom"></div>
    <div class="contact">
      <p class="contact__name">Dr. Marcus Delaven, D.D.S</p>
      <p class="contact__title">Oral &amp; Maxillofacial Sugery</p>
      <p class="contact__line">555-210-4700</p>
      <p class="contact__line">555-210-5006</p>
      <p class="contact__line">HalveringOralSurgeon@mailbox.example</p>
      <p class="contact__line">www.HalveringOralSurgeryCenter.example</p>
      <p class="contact__address">2840 Larkmoor Ave | Halvering, NY 11990</p>
    </div>
  </section>

  <section class="card card--brand">
    <div class="tab tab--right"></div>
    <div class="tab tab--left"></div>
    <div class="brand">
      <div class="brand__illustration" role="img" aria-label="Practice emblem illustration area"></div>
      <p class="brand__name">
        <span class="brand__line">Halvering</span>
        <span class="brand__line">Oral Surgery &amp;</span>
        <span class="brand__line">Implant Center</span>
      </p>
    </div>
    <div class="social">
      <p class="social__item"><span class="social__dot"></span>HalveringSurgeon</p>
      <p class="social__item"><span class="social__dot social__dot--round"></span>Halvering Oral Surgery &amp; Implant Center</p>
    </div>
  </section>
</main>
</body>
</html>
```